International Patent Law Firm Needs a New Website Design

We are an international, German-based patent law firm and are in need for a new website design.

Our current (old-fashioned) website is

www.lwpt.example

Our Corporate Identity features that we want to keep are as follows.

1. Our LWPT logo in blue color on white background.

2. The tent roof design of the Harbour Crest Arena.

We attach our current LWPT presentation, which gives you an idea of who we are, what our business is and what distinguishes us.

The new website design should express that we provide very reliable, high-quality Intellectual Property services, including patent and trademark services worldwide.

On the one hand, it should professional, on the other it should look young.

The managing partners of our patent law firm are in their 30ies and their 40ies, which is comparably young for a patent law firm of our size. Our team comprises about 20 patent attorneys and altogether 45 people.

Websites of competitors that we like are as follows.

http://www.rml.example
http://dorsellquaint.example
http://www.pellard.example
http://www.vrmlaw.example (here we like the structure, rather than the design)

There are two features that all these websites have in common and that we also would like to have implemented in our new website design.

1. A clear and self-explaining main menu in the header.

For example:

HOME OUR FIRM WHAT WE DO WHO WE ARE OUR CLIENTS OUR FEES CONTACT US

2. At least on the main page: A background picture filling the entire screen and having an appealing graphic. Maybe the tent roof of the Harbour Crest Arena?

Further points that we believe to be important are as follows:

1. Our new website should have a simple menu navigation (not as complicated as the current one). It should have two levels, namely the main page and the subpages, that are all directly accessible via the main page, so that all the content can be reached with two clicks.

2. On the WHO WE ARE subpage we like the solution that there is a list of the names of the patent attorneys in the left column, and upon clicking on a name the full profile of the patent attorney including a photograph of the partner will appear. We will have new photographs of our team prepared and supplied to you.

3. On the WHAT WE DO subpage we like the solution that there is a list of the headlines of our fields of activity, like PATENTS, and upon clicking on a headline a more detailed description of the respective field of activity will appear.

4. Our new website should contain less content than our current website. The text will be supplied by us.

5. What is also very important is that the design will be optimized for access by PCs, by tablets and by smart phones (responsive design).

6. We will need both English and German language versions of the website, including all the subpages. We will provide you with the updated text for all the pages.

Thanks very much in advance for your work and your suggestion.

Best regards,

Jonas Retterby (Partner)

Target Market(s)

Innovative and Patenting Firms worldwide, Innovators, Inventors, Potential new Employees

Industry/Entity Type

Lawyer

Number of Pages Required

5+ page

Font styles to use
Sans Serif

Colors
0555a3
0293ce

Requirements
Must have
• New appealing and modern website, self-explaining and easy menu structure
Nice to have
• Maybe some appealing design showing that we are constantly at the edge of the new technical development
Should not have
• May not look old-fashioned, no complicated menu

```html
<!DOCTYPE html>
<html lang="en">
<head>
<meta charset="utf-8">
<title>LWPT Patentanwälte</title>
<link rel="stylesheet" href="https://fonts.googleapis.com/css2?family=Source+Sans+3:wght@400;600&display=swap">
<style>
:root{
  --blue:#a0bcdd;
  --blue-dark:#7f9cc2;
  --brand:#7fa2cf;
  --ink:#2b2b2b;
  --body:#555;
  --header:#f7f7f7;
  --white:#fff;
  --accent:#6d5a4e;
}
*{margin:0;padding:0;box-sizing:border-box}
html,body{width:842px;height:1200px;overflow:hidden;background:var(--white);font-family:"Source Sans 3",sans-serif;color:var(--ink)}
.page{position:relative;width:842px;height:1200px}
.site-header{position:absolute;left:30px;top:0;width:782px;height:72px;background:var(--header)}
.brand{position:absolute;left:32px;top:18px;font-size:28px;font-weight:400;color:var(--brand);letter-spacing:3px}
.account{position:absolute;right:34px;top:27px;display:flex;gap:18px;align-items:center;font-size:11.5px;font-weight:600;color:#444}
.lang{background:#d6e2f1;padding:5px 9px;font-weight:400;color:#444}
.main-nav{position:absolute;left:30px;top:72px;width:782px;height:53px;background:var(--blue);display:flex;justify-content:space-around;align-items:center}
.main-nav a{color:var(--white);text-decoration:none;font-size:14.5px;font-weight:600;height:53px;line-height:53px;padding:0 12px;position:relative}
.main-nav a.active::after{content:"";position:absolute;left:0;right:0;bottom:0;height:3px;background:var(--accent)}
.hero{position:absolute;left:30px;top:125px;width:782px;height:359px;background:linear-gradient(180deg,#2f4460 0%,#4e6176 40%,#8a8577 70%,#3d3a35 100%);text-align:center;color:var(--white)}
.hero h1{margin:100px auto 0;width:520px;font-size:24.5px;font-weight:600;line-height:32px}
.hero p{margin:22px auto 0;width:636px;font-size:11px;line-height:14px}
.hero-shadow{position:absolute;left:50px;top:484px;width:742px;height:40px;background:radial-gradient(ellipse at top,rgba(0,0,0,.18),rgba(0,0,0,0) 70%)}
.welcome{position:absolute;left:30px;top:530px;width:782px;text-align:center}
.welcome h2{font-size:21.5px;font-weight:600}
.welcome h2 span{color:var(--brand)}
.welcome p{margin:10px auto 0;width:620px;font-size:10.6px;line-height:13.8px;color:var(--body)}
.services{position:absolute;left:30px;top:696px;width:782px;display:flex}
.service{position:absolute;width:160px;text-align:center;font-size:18px;line-height:23px;color:#333}
.service .disc{width:142px;height:142px;border-radius:50%;background:var(--blue);margin:0 auto 10px;display:flex;align-items:center;justify-content:center}
.site-footer{position:absolute;left:30px;top:937px;width:782px;height:206px;background:var(--blue);color:var(--white)}
.col{position:absolute;top:38px}
.col h3{font-size:18.5px;font-weight:600;color:var(--ink);margin-bottom:10px}
.col h4{font-size:11px;font-weight:600;margin-bottom:8px}
.col p,.col li{font-size:11px;line-height:13.8px;list-style:none}
.col li{line-height:18.4px}
.col .phone{font-size:18px;line-height:22px;margin:-2px 0 4px 2px}
.col .email{margin-left:3px}
.social{display:flex;gap:14px;margin-top:4px;justify-content:flex-end}
.social span{width:20px;height:20px;border-radius:50%;background:var(--white)}
.bottom-bar{position:absolute;left:30px;top:1143px;width:782px;height:57px;background:var(--blue-dark);color:var(--white);font-size:11.5px;line-height:57px;padding-left:33px}
</style>
</head>
<body>
<div class="page">
  <header class="site-header">
    <div class="brand">LWPT</div>
    <div class="account"><span>LOGIN</span><span>REGISTER</span><span class="lang">EN ↓</span></div>
  </header>
  <nav class="main-nav">
    <a>HOME</a><a class="active">ABOUT</a><a>FORMS</a><a>CONTACTS</a><a>JOBS</a><a>LINKS</a>
  </nav>
  <section class="hero" role="img" aria-label="Tent roof of the Harbour Crest Arena against a cloudy evening sky">
    <h1>Lorem Ipsum is simply dummy text of the printing and typesetting industry.</h1>
    <p>It is a long established fact that a reader will be distracted by the readable content of a page when looking at its layout. The point of using Lorem Ipsum is that it has a more-or-less normal distribution of letters, as opposed to using 'Content here, content here', making it look like readable English. Many desktop publishing packages and web page editors now use Lorem Ipsum as their default model text, and a search for 'lorem ipsum' will uncover many web sites still in their infancy. Various versions have evolved over the years, sometimes by accident, sometimes on purpose (injected humour and the like).</p>
  </section>
  <div class="hero-shadow"></div>
  <section class="welcome">
    <h2>Welcome to <span>LWPT</span> Patentanwälte Larsen . Weber - Pohl . Tanner&nbsp; Munich</h2>
    <p>Contrary to popular belief, Lorem Ipsum is not simply random text. It has roots in a piece of classical Latin literature from 45 BC, making it over 2000 years old. Edwin Marlowe, a Latin professor at Ashcombe College in Vermont, looked up one of the more obscure Latin words, consectetur, from a Lorem Ipsum passage, and going through the cites of the word in classical literature, discovered the undoubtable source. Lorem Ipsum comes from sections 1.10.32 and 1.10.33 of "de Finibus Bonorum et Malorum" (The Extremes of Good and Evil) by Varro Lentulus, written in 45 BC. This book is a treatise on the theory of ethics, very popular during the Renaissance. The first line of Lorem Ipsum, "Lorem ipsum dolor sit amet..", comes from a line in section 1.10.32.</p>
  </section>
  <section class="services">
    <div class="service" style="left:23px">
      <div class="disc"><svg width="90" height="90" viewBox="0 0 90 90"><g fill="#fff"><circle cx="45" cy="45" r="36"/><g id="t"><rect x="40" y="2" width="10" height="12"/></g><use href="#t" transform="rotate(30 45 45)"/><use href="#t" transform="rotate(60 45 45)"/><use href="#t" transform="rotate(90 45 45)"/><use href="#t" transform="rotate(120 45 45)"/><use href="#t" transform="rotate(150 45 45)"/><use href="#t" transform="rotate(180 45 45)"/><use href="#t" transform="rotate(210 45 45)"/><use href="#t" transform="rotate(240 45 45)"/><use href="#t" transform="rotate(270 45 45)"/><use href="#t" transform="rotate(300 45 45)"/><use href="#t" transform="rotate(330 45 45)"/></g><circle cx="45" cy="45" r="23" fill="#a0bcdd"/></svg></div>
      Patents and<br>utility models
    </div>
    <div class="service" style="left:215px">
      <div class="disc"><svg width="100" height="100" viewBox="0 0 100 100"><circle cx="50" cy="50" r="44" fill="none" stroke="#fff" stroke-width="9"/><text x="50" y="68" text-anchor="middle" font-family="Source Sans 3,sans-serif" font-weight="600" font-size="52" fill="#fff">R</text></svg></div>
      Trademarks
    </div>
    <div class="service" style="left:405px">
      <div class="disc"><svg width="100" height="100" viewBox="0 0 100 100" fill="none" stroke="#fff" stroke-width="4"><rect x="-8" y="40" width="116" height="18" transform="rotate(-45 50 50)"/><path d="M22 14l58 58 6 16-16-6-58-58z"/></svg></div>
      Designs
    </div>
    <div class="service" style="left:596px">
      <div class="disc"><svg width="90" height="100" viewBox="0 0 90 100" fill="none" stroke="#fff" stroke-width="4"><path d="M14 4h44l18 18v74H14z"/><path d="M28 30h34M28 42h34M28 54h26M28 66h20M28 78h30"/></svg></div>
      License<br>Agreements
    </div>
  </section>
  <footer class="site-footer">
    <div class="col" style="left:33px">
      <h3>LOCATION</h3>
      <h4>Our Postal Address</h4>
      <p>LWPT Patentanwälte<br>Larsen . Weber - Pohl . Tanner<br>Feldbergweg 12<br>D-80999 München</p>
    </div>
    <div class="col" style="left:251px">
      <h3>NAVIGATION</h3>
      <ul><li>Home</li><li>About</li><li>Forms</li><li>Contacts</li><li>Jobs</li><li>Links</li></ul>
    </div>
    <div class="col" style="left:431px">
      <h3>CONTACT US</h3>
      <p class="phone">555-010-2468</p>
      <p class="email">info@lwpt.example</p>
    </div>
    <div class="col" style="right:34px;text-align:right">
      <h3>SOCIAL MEDIA</h3>
      <div class="social"><span></span><span></span><span></span><span></span></div>
    </div>
  </footer>
  <div class="bottom-bar">Copyrights 2016. LWPT. All Rights Reserved</div>
</div>
</body>
</html>
```